Business Card Design

Mobile dog grooming

Industry/Entity Type

Business

Contact Information for Business Card

Tidewell Pawcraft Mobile Grooming
Marisol Pettery
555-314-2976
www.tidewellpawcraftgrooming.example

```html
<!DOCTYPE html>
<html lang="en">
<head>
<meta charset="utf-8">
<title>Tidewell Pawcraft Mobile Grooming — Business Card</title>
<link rel="stylesheet" href="https://fonts.googleapis.com/css2?family=Oswald:wght@400;500&family=Open+Sans:wght@400;600&display=swap">
<style>
  :root {
    --page-bg: #e9e9ec;
    --card-bg: #ffffff;
    --brand-purple: #8a63b8;
    --deep-purple: #7a52ab;
    --ink-gray: #4a4a4a;
    --ink-dark: #2b2b2b;
    --art-blue: #bfe0f5;
    --art-cream: #f1e3c6;
    --white: #ffffff;
  }
  * { margin: 0; padding: 0; box-sizing: border-box; }
  html, body {
    width: 1200px;
    height: 900px;
    overflow: hidden;
    background: var(--page-bg);
  }
  .stage {
    width: 1200px;
    height: 900px;
    display: flex;
    align-items: center;
    justify-content: center;
  }
  .card {
    position: relative;
    width: 460px;
    height: 800px;
    background: var(--card-bg);
    border-radius: 26px;
    overflow: hidden;
    box-shadow: 0 6px 24px rgba(0,0,0,0.12);
  }
  .brand-art {
    position: absolute;
    left: 50px;
    top: 60px;
    width: 360px;
    height: 200px;
    border-radius: 18px;
    background: linear-gradient(135deg, var(--art-blue) 0%, #e8f2fa 45%, var(--art-cream) 100%);
  }
  .brand-name {
    position: absolute;
    left: 0;
    right: 0;
    top: 278px;
    text-align: center;
    font-family: "Oswald", sans-serif;
    font-weight: 500;
    font-size: 30px;
    line-height: 1.15;
    letter-spacing: 0.5px;
    text-transform: uppercase;
    color: var(--brand-purple);
  }
  .divider {
    position: absolute;
    left: 0;
    top: 392px;
    width: 460px;
    height: 24px;
  }
  .contact-name {
    position: absolute;
    left: 0;
    right: 0;
    top: 530px;
    text-align: center;
    font-family: "Oswald", sans-serif;
    font-weight: 400;
    font-size: 34px;
    text-transform: uppercase;
    letter-spacing: 0.5px;
  }
  .contact-name .first { color: var(--brand-purple); }
  .contact-name .last { color: var(--ink-gray); }
  .contact-phone {
    position: absolute;
    left: 0;
    right: 0;
    top: 594px;
    text-align: center;
    font-family: "Open Sans", sans-serif;
    font-size: 21px;
    color: var(--ink-dark);
  }
  .footer-band {
    position: absolute;
    left: 0;
    bottom: 0;
    width: 460px;
    height: 130px;
  }
  .website {
    position: absolute;
    left: 0;
    right: 0;
    bottom: 34px;
    text-align: center;
    font-family: "Open Sans", sans-serif;
    font-weight: 600;
    font-size: 17px;
    color: var(--white);
  }
</style>
</head>
<body>
  <main class="stage">
    <article class="card">
      <div class="brand-art" role="img" aria-label="Cartoon illustration of dogs in a bubbly grooming tub on wheels"></div>
      <div class="brand-name">Tidewell Pawcraft<br>Mobile Grooming</div>

      <svg class="divider" viewBox="0 0 460 24" aria-hidden="true">
        <polyline points="0,10 216,10 230,20 244,10 460,10" fill="none" stroke="var(--brand-purple)" stroke-width="2"/>
      </svg>

      <h1 class="contact-name"><span class="first">Marisol</span> <span class="last">Pettery</span></h1>
      <p class="contact-phone">555-314-2976</p>

      <svg class="footer-band" viewBox="0 0 460 130" preserveAspectRatio="none" aria-hidden="true">
        <path d="M0,20 Q230,-8 460,20 L460,130 L0,130 Z" fill="var(--brand-purple)"/>
      </svg>
      <p class="website">www.tidewellpawcraftgrooming.example</p>
    </article>
  </main>
</body>
</html>
```